Graphic Design for a block-note A4 size

We need a graphic design for a simple block-note A4 size. The product consists of 50 sheets in VERTICAL A4 (21x29,7cm) size, simply glued on top, without cover. We would like to have proposals with double application: one for home users without a logo and one for professionals with an area "put your logo here".
The graphics should be simple and attractive, elegant and pleasant to keep on your desk.
The block-notes may have standard squares (5 or 10 mm) or stripes (10 mm spaced) on the background to make the writing easy.
Feel free to use your creativity, the only limit is the CMYK color space.

We will upload some block-note simple templates and 3D sample images to help you.

• The graphics should be simple and attractive, elegant and pleasant to keep on your desk.

• The block-notes may have standard squares (5 or 10 mm) or stripes (10 mm spaced) on the background to make the writing easy.

```html
<!DOCTYPE html>
<html lang="en">
<head>
<meta charset="utf-8">
<title>A4 Block-Note – Squared Sheet with Logo Area</title>
<link rel="stylesheet" href="https://fonts.googleapis.com/css2?family=Arimo:wght@400&display=swap">
<style>
  :root {
    --backdrop: #ffffff;
    --frame: #1c1a1a;
    --frame-edge: #3a3838;
    --sheet: #ffffff;
    --sheet-rim: #bdbdbd;
    --grid-line: #b9b9b9;
    --gloss: #e9e9e9;
    --bar-dark: #1e1e1e;
    --bar-light: #6b6b6b;
    --ink: #2a2a2a;
    --button: #d9d9d9;
  }
  html, body {
    margin: 0;
    padding: 0;
    width: 1200px;
    height: 900px;
    overflow: hidden;
    background: var(--backdrop);
  }
  .canvas {
    display: block;
    width: 1200px;
    height: 900px;
  }
  .brand-name {
    font-family: "Arimo", Arial, sans-serif;
    font-weight: 400;
    fill: var(--ink);
  }
</style>
</head>
<body>
<svg class="canvas" width="1200" height="900" viewBox="0 0 1200 900" xmlns="http://www.w3.org/2000/svg" aria-label="A4 squared block-note sheet with a brand area">
  <defs>
    <pattern id="grid-squares" x="325" y="54" width="14" height="14" patternUnits="userSpaceOnUse">
      <path d="M14 0 H0 V14" fill="none" stroke="var(--grid-line)" stroke-width="1"/>
    </pattern>
    <linearGradient id="brand-bar-fill" x1="0" y1="0" x2="0" y2="1">
      <stop offset="0" stop-color="var(--bar-light)"/>
      <stop offset="0.45" stop-color="var(--bar-dark)"/>
      <stop offset="1" stop-color="var(--bar-dark)"/>
    </linearGradient>
    <linearGradient id="frame-fill" x1="0" y1="0" x2="1" y2="0">
      <stop offset="0" stop-color="var(--frame-edge)"/>
      <stop offset="0.04" stop-color="var(--frame)"/>
      <stop offset="0.96" stop-color="var(--frame)"/>
      <stop offset="1" stop-color="var(--frame-edge)"/>
    </linearGradient>
    <clipPath id="sheet-clip">
      <rect x="325" y="54" width="550" height="777" rx="16"/>
    </clipPath>
  </defs>

  <!-- notepad frame -->
  <g class="notepad">
    <rect class="notepad-frame" x="306" y="40" width="588" height="820" rx="10" fill="url(#frame-fill)"/>
    <rect class="frame-sheen" x="880" y="54" width="8" height="130" rx="3" fill="#8a8a8a" opacity="0.7"/>

    <!-- writing sheet -->
    <g class="sheet" clip-path="url(#sheet-clip)">
      <rect x="325" y="54" width="550" height="777" fill="var(--sheet)"/>
      <path class="sheet-gloss" d="M325 500 C 520 470, 700 390, 875 300 V831 H325 Z" fill="var(--gloss)"/>
      <rect class="sheet-grid" x="325" y="54" width="550" height="777" fill="url(#grid-squares)"/>
    </g>
    <rect class="sheet-rim" x="325" y="54" width="550" height="777" rx="16" fill="none" stroke="var(--sheet-rim)" stroke-width="3"/>

    <!-- brand area -->
    <rect class="brand-bar" x="344" y="724" width="333" height="72" rx="6" fill="url(#brand-bar-fill)"/>
    <text class="brand-name" x="773" y="769" font-size="24" text-anchor="middle">Quadra Notes</text>

    <!-- base button -->
    <rect class="home-button" x="591" y="836" width="17" height="17" rx="4" fill="none" stroke="var(--button)" stroke-width="2"/>
  </g>
</svg>
</body>
</html>
```